Vardel Precision New Website Design

We just changed our logo (thank you ArtFolkly) and company name change from Vardel Precision Machining to Vardel Precision Manufacturing. We do CNC Swiss screw machining and multi-axis machines. We make parts for many industries. We make large quantity production parts as well small R&D quantities. You can look at our current (outdated) website: http://www.vardelprecisionmachining.example to see what we do. We would like a WordPress site, including contact form for "request for quote" . We would also like it to be mobile friendly, and the ability to maintain it ourselves after it is finished I have included our new logo and fonts for references. We would like our site to convey the feeling of precision, capability, and trust worthiness with a very modern look. The new website address is www.vardelprec-mfg.example

Font styles to use
Serif
Sans Serif
Other font styles liked:
• fronts included, not sure if they work

Colors

Designer to choose colors to be used in the design.

Requirements
Must have
• Contact Info, request for quote field

```html
<!DOCTYPE html>
<html lang="en">
<head>
<meta charset="utf-8">
<title>Vardel Precision Manufacturing</title>
<link rel="stylesheet" href="https://fonts.googleapis.com/css2?family=Montserrat:wght@400;500;600;700&family=Bebas+Neue&display=swap">
<style>
:root{
  --blue:#1d3a8a;
  --blue-dark:#16307a;
  --ink:#2b2b2b;
  --muted:#555;
  --grey-panel:#efefef;
  --footer:#3b3b3b;
  --footer-text:#d8d8d8;
  --white:#fff;
}
*{box-sizing:border-box;margin:0;padding:0}
html,body{width:1200px;height:3981px;overflow:hidden}
body{position:relative;background:var(--white);font-family:'Montserrat',sans-serif;color:var(--ink)}
.abs{position:absolute}

/* header */
.site-header{position:absolute;left:0;top:0;width:1200px;height:105px;background:var(--white)}
.brand{position:absolute;left:172px;top:28px;display:flex;align-items:center;gap:10px}
.brand-dot{width:22px;height:22px;border-radius:50%;background:var(--blue)}
.brand-name{font-weight:700;font-size:21px;color:var(--blue);line-height:1.05;letter-spacing:.5px}
.brand-name small{display:block;font-size:11px;letter-spacing:2px}
.phone{position:absolute;right:174px;top:22px;font-size:20px;font-weight:600;color:var(--blue);display:flex;align-items:center;gap:10px}
.main-nav{position:absolute;right:176px;top:67px;display:flex;gap:33px;font-size:13px;font-weight:500;color:var(--ink)}

/* hero */
.hero{position:absolute;left:0;top:105px;width:1200px;height:635px;background:linear-gradient(100deg,#5b6c86 0%,#8a95a8 30%,#b49a6a 38%,#6f7d96 55%,#9aa6b8 80%,#c9d0da 100%)}
.hero-title{position:absolute;left:580px;top:212px;font-family:'Bebas Neue',sans-serif;font-size:78px;line-height:.92;color:var(--white)}
.slider-dots{position:absolute;left:512px;top:570px;display:flex;gap:5px}
.slider-dots span{width:41px;height:4px;background:var(--white)}
.slider-dots span.dim{opacity:.5}

/* about */
.about-panel{position:absolute;left:0;top:740px;width:598px;height:680px;background:var(--grey-panel)}
.photo-frame{position:absolute;background:var(--white);padding:9px}
.photo-frame div{width:100%;height:100%}
.section-title{font-weight:700;font-size:27px;letter-spacing:.5px}
.about-text{position:absolute;left:697px;top:880px;width:330px}
.about-text p{font-size:12.5px;line-height:22.5px;color:var(--muted);margin-top:14px}
.about-text p+p{margin-top:20px}
.btn-outline{display:inline-block;margin-top:26px;border:2px solid var(--ink);border-radius:20px;padding:8px 22px;font-size:12px;font-weight:700;letter-spacing:.5px}

/* industries */
.band{position:absolute;left:0;top:0}
.industries-title{position:absolute;left:0;width:1200px;top:1495px;text-align:center;color:var(--white)}
.industry{position:absolute;top:1579px;width:124px;text-align:center;color:var(--white);font-size:16px}
.industry .ring{width:106px;height:106px;margin:0 auto 12px;border:2px solid var(--white);border-radius:50%;display:flex;align-items:center;justify-content:center}

/* services */
.services-title{position:absolute;left:0;width:1200px;top:1907px;text-align:center}
.service-photo{position:absolute;width:296px;height:296px;border-radius:50%;border:5px solid var(--blue)}
.service-text{position:absolute;width:455px}
.service-text h3{font-weight:500;font-size:27px}
.service-text p{margin-top:16px;padding-left:7px;font-size:12.5px;line-height:20.5px;color:var(--muted)}

/* quote */
.quote-title{position:absolute;left:0;width:1200px;top:3098px;text-align:center;color:var(--white)}
.quote-sub{position:absolute;left:0;width:1200px;top:3142px;text-align:center;color:#cfd6ea;font-size:16px}
.field{position:absolute;background:var(--white);font-size:11px;color:#777;padding:10px 8px}
.btn-submit{position:absolute;left:539px;top:3315px;width:121px;height:42px;border:2px solid var(--white);border-radius:21px;background:#232323;color:var(--white);font-size:13px;font-weight:700;letter-spacing:1.5px;display:flex;align-items:center;justify-content:center}

/* testimonial */
.quote-mark{position:absolute;left:295px;top:3528px;width:80px;height:80px;border-radius:50%;background:var(--blue);color:var(--white);font-size:70px;font-weight:700;display:flex;align-items:center;justify-content:center;line-height:1;padding-top:26px}
.testimonial{position:absolute;left:411px;top:3534px;width:540px;font-size:15px;line-height:22px;color:var(--ink)}
.testimonial cite{display:block;margin-top:12px;font-style:normal;font-weight:600}

/* footer */
.site-footer{position:absolute;left:0;top:3690px;width:1200px;height:291px;background:var(--footer);color:var(--footer-text)}
.footer-brand{position:absolute;left:172px;top:46px;display:flex;align-items:center;gap:10px}
.footer-brand .brand-name{color:var(--white);font-size:19px}
.footer-brand .brand-dot{background:var(--white)}
.footer-about{position:absolute;left:172px;top:118px;width:250px;font-size:11.5px;line-height:21px}
.footer-col h4{font-weight:400;font-size:18px;color:var(--white);margin-bottom:12px}
.footer-col{position:absolute;top:40px;font-size:11.5px;line-height:21px}
.footer-col ul{list-style:none}
.contact-row{display:flex;gap:8px;align-items:flex-start}
.contact-row svg{margin-top:5px;flex:none}
.social{display:flex;gap:6px}
.social span{width:24px;height:24px;border-radius:50%;background:#3f66c4}
.badges{display:flex;gap:14px;margin-top:40px;align-items:center}
.footer-rule{position:absolute;left:172px;top:240px;width:856px;height:1px;background:#555}
.copyright{position:absolute;left:0;width:1200px;top:258px;text-align:center;font-size:10.5px}
</style>
</head>
<body>

<header class="site-header">
  <div class="brand"><span class="brand-dot"></span><span class="brand-name">VARDEL PRECISION<small>MANUFACTURING</small></span></div>
  <div class="phone">
    <svg width="16" height="16" viewBox="0 0 24 24"><path fill="#1d3a8a" d="M6.6 10.8a15 15 0 0 0 6.6 6.6l2.2-2.2c.3-.3.7-.4 1-.2 1.1.4 2.3.6 3.6.6.6 0 1 .4 1 1V20c0 .6-.4 1-1 1A17 17 0 0 1 3 4c0-.6.4-1 1-1h3.5c.6 0 1 .4 1 1 0 1.3.2 2.5.6 3.6.1.3 0 .7-.2 1z"/></svg>
    Telephone:555-014-2270
  </div>
  <nav class="main-nav"><span>Home</span><span>Services</span><span>Equipment</span><span>Quality</span><span>Our work</span><span>About us</span><span>Contact us</span></nav>
</header>

<section class="hero" role="img" aria-label="Close-up photo of a CNC machine spindle cutting metal with coolant">
  <h1 class="hero-title">VARDEL PRECISION<br>MANUFACTURING</h1>
  <div class="slider-dots"><span></span><span></span><span class="dim"></span><span></span></div>
</section>

<div class="about-panel"></div>

<svg class="band" width="1200" height="3981" viewBox="0 0 1200 3981" aria-hidden="true">
  <polygon points="0,1420 1200,1368 1200,1817 0,1868" fill="#1d3a8a"/>
  <polygon points="0,3045 1200,2963 1200,3478 0,3478" fill="#1d3a8a"/>
</svg>

<div class="photo-frame" style="left:140px;top:845px;width:330px;height:300px"><div role="img" aria-label="Photo of a lathe chuck turning a metal part" style="background:linear-gradient(90deg,#4a4a4a,#bdbdbd 40%,#7a7a7a 70%,#d8d8d8)"></div></div>
<div class="photo-frame" style="left:316px;top:925px;width:347px;height:385px"><div role="img" aria-label="Photo of the open door of a CNC turning centre with its control panel" style="background:linear-gradient(110deg,#cfcfcf,#8d8d8d 45%,#3a3a3a 75%,#6b6b6b)"></div></div>

<div class="about-text">
  <h2 class="section-title">ABOUT US</h2>
  <p>Vardel Precision Manufacturing Company is a high quality machining resource providing friendly service, fast turnaround times, and engineering expertise, at competitive pricing. With almost 20 years of experience in the industry, Vardel Precision utilizes certified state of the art equipment partnered with top professionals to maximize the value and quality in your product.</p>
  <p>Specializing in precision, Vardel Precision will provide you with superior products, at affordable prices.</p>
  <span class="btn-outline">READ MORE</span>
</div>

<h2 class="section-title industries-title">INDUSTRIES SERVED</h2>
<div class="industry" style="left:167px"><div class="ring"><svg width="54" height="54" viewBox="0 0 48 48" fill="none" stroke="#fff" stroke-width="2" stroke-linejoin="round"><path d="M38 10 22 26M40 8c-2-2-5 0-7 2l-5 5-16-4-3 3 13 7-6 7-5-1-2 2 6 3 3 6 2-2-1-5 7-6 7 13 3-3-4-16 5-5c2-2 4-5 2-7z"/></svg></div>Aerospace</div>
<div class="industry" style="left:291px"><div class="ring"><svg width="54" height="54" viewBox="0 0 48 48" fill="none" stroke="#fff" stroke-width="2"><rect x="16" y="16" width="16" height="16"/><rect x="21" y="21" width="6" height="6"/><path d="M20 16V8M28 16V8M20 32v8M28 32v8M16 20H8M16 28H8M32 20h8M32 28h8"/><circle cx="20" cy="6" r="2"/><circle cx="28" cy="6" r="2"/><circle cx="20" cy="42" r="2"/><circle cx="28" cy="42" r="2"/><circle cx="6" cy="20" r="2"/><circle cx="6" cy="28" r="2"/><circle cx="42" cy="20" r="2"/><circle cx="42" cy="28" r="2"/></svg></div>Electronics</div>
<div class="industry" style="left:415px"><div class="ring"><svg width="54" height="54" viewBox="0 0 48 48" fill="none" stroke="#fff" stroke-width="2"><circle cx="14" cy="33" r="7"/><circle cx="14" cy="33" r="3"/><circle cx="35" cy="35" r="5"/><path d="M10 25V14h14l4 11h8l3 6M20 14v11M33 15v10"/></svg></div>Automotive</div>
<div class="industry" style="left:539px"><div class="ring"><svg width="54" height="54" viewBox="0 0 48 48" fill="none" stroke="#fff" stroke-width="2.5" stroke-linecap="round"><circle cx="24" cy="8" r="3"/><path d="M24 11v30M16 18h16M8 28c0 8 8 13 16 13s16-5 16-13M8 28l-3 3M8 28l3 3M40 28l-3 3M40 28l3 3"/></svg></div>Marine</div>
<div class="industry" style="left:663px"><div class="ring"><svg width="54" height="54" viewBox="0 0 48 48" fill="none" stroke="#fff" stroke-width="2"><rect x="7" y="9" width="34" height="22" rx="1"/><path d="M7 26h34M20 31l-2 8M28 31l2 8M14 39h20M19 19l5-5M23 21l6-6"/></svg></div>Computer</div>
<div class="industry" style="left:787px"><div class="ring"><svg width="54" height="54" viewBox="0 0 48 48" fill="none" stroke="#fff" stroke-width="2" stroke-linejoin="round"><path d="M24 41 9 27a9 9 0 0 1 15-12 9 9 0 0 1 15 12z"/><path d="M21 19h6v5h5v6h-5v5h-6v-5h-5v-6h5z"/></svg></div>Medical</div>
<div class="industry" style="left:911px"><div class="ring"><svg width="54" height="54" viewBox="0 0 48 48" fill="none" stroke="#fff" stroke-width="2" stroke-linejoin="round"><path d="M15 7c-6 0-9 5-8 11 1 5 3 7 4 12l3 11c1 2 3 2 4 0l3-10c1-2 5-2 6 0l3 10c1 2 3 2 4 0l3-11c1-5 3-7 4-12 1-6-2-11-8-11-4 0-5 2-9 2s-5-2-9-2z"/></svg></div>Dental</div>

<h2 class="section-title services-title">WHAT WE DO</h2>

<div class="service-photo" style="left:220px;top:1979px;background:radial-gradient(circle at 45% 55%,#d7d7d7,#7d7d7d 55%,#3c3c3c)" role="img" aria-label="Photo of a Swiss screw machine tool cutting a small metal part"></div>
<div class="service-text" style="left:539px;top:2020px">
  <h3>CNC Swiss Screw Machining</h3>
  <p>At vero eos et accusamus et iusto odio dignissimos ducimus qui blanditiis praesentium voluptatum deleniti atque corrupti quos dolores et quas molestias excepturi sint occaecati cupiditate non provident, similique sunt in culpa qui officia deserunt mollitia animi, id est laborum et dolorum fuga. Et harum quidem rerum facilis est et expedita distinctio. Nam libero tempore, cum soluta nobis est eligendi optio cumque nihil impedit quo minus</p>
</div>

<div class="service-text" style="left:172px;top:2336px">
  <h3>Multi-Axis Machines</h3>
  <p>At vero eos et accusamus et iusto odio dignissimos ducimus qui blanditiis praesentium voluptatum deleniti atque corrupti quos dolores et quas molestias excepturi sint occaecati cupiditate non provident, similique sunt in culpa qui officia deserunt mollitia animi, id est laborum et dolorum fuga. Et harum quidem rerum facilis est et expedita distinctio. Nam libero tempore, cum soluta nobis est eligendi optio cumque nihil impedit quo minus</p>
</div>
<div class="service-photo" style="left:684px;top:2293px;background:linear-gradient(180deg,#9a9ea4,#5e646c 50%,#2f3338)" role="img" aria-label="Photo of a shop floor with rows of multi-axis machines"></div>

<div class="service-photo" style="left:220px;top:2617px;background:linear-gradient(90deg,#bfb7a8,#e6dfd0 45%,#6a6a6a 70%,#2b2b2b)" role="img" aria-label="Photo of an inspection station with a measuring machine and monitor"></div>
<div class="service-text" style="left:539px;top:2662px">
  <h3>Small R&amp;D quantities</h3>
  <p>At vero eos et accusamus et iusto odio dignissimos ducimus qui blanditiis praesentium voluptatum deleniti atque corrupti quos dolores et quas molestias excepturi sint occaecati cupiditate non provident, similique sunt in culpa qui officia deserunt mollitia animi, id est laborum et dolorum fuga. Et harum quidem rerum facilis est et expedita distinctio. Nam libero tempore, cum soluta nobis est eligendi optio cumque nihil impedit quo minus</p>
</div>

<h2 class="section-title quote-title">REQUEST FOR QUOTE</h2>
<p class="quote-sub">Lorem ipsum dolor sit amet, consectetur adipiscing</p>
<div class="field" style="left:286px;top:3188px;width:312px;height:34px">Name:</div>
<div class="field" style="left:286px;top:3228px;width:312px;height:34px">Email:</div>
<div class="field" style="left:286px;top:3268px;width:312px;height:35px">Phone:</div>
<div class="field" style="left:611px;top:3188px;width:312px;height:116px">Request</div>
<div class="btn-submit">SUBMIT</div>

<div class="quote-mark">“</div>
<blockquote class="testimonial">"I love working with engineers. Finding ways to make their parts less expensive is a puzzle I never get tired of solving."
  <cite>Tobias Lindqvist &nbsp; Founder</cite>
</blockquote>

<footer class="site-footer">
  <div class="footer-brand"><span class="brand-dot"></span><span class="brand-name">VARDEL PRECISION<small>MANUFACTURING</small></span></div>
  <p class="footer-about">At vero eos et accusamus et iusto odio dignissimos ducimus qui blanditiis praesentium voluptatum deleniti atque corrupti quos dolores et quas molestias excepturi sint occaecati cupiditate</p>

  <div class="footer-col" style="left:486px">
    <h4>Links</h4>
    <ul><li>Home</li><li>Services</li><li>Equipment</li><li>Quality</li><li>Our work</li><li>About us</li><li>Contact us</li></ul>
  </div>

  <div class="footer-col" style="left:659px">
    <h4>Contact</h4>
    <div class="contact-row"><svg width="8" height="11" viewBox="0 0 10 14"><path fill="#d8d8d8" d="M5 0a5 5 0 0 0-5 5c0 4 5 9 5 9s5-5 5-9a5 5 0 0 0-5-5zm0 7a2 2 0 1 1 0-4 2 2 0 0 1 0 4z"/></svg><span>Vardel Precision Machining<br>4410 Calloway Ave.<br>Fernbrook, CA 90000</span></div>
    <div class="contact-row"><svg width="9" height="9" viewBox="0 0 24 24"><path fill="#d8d8d8" d="M6.6 10.8a15 15 0 0 0 6.6 6.6l2.2-2.2c.3-.3.7-.4 1-.2 1.1.4 2.3.6 3.6.6.6 0 1 .4 1 1V20c0 .6-.4 1-1 1A17 17 0 0 1 3 4c0-.6.4-1 1-1h3.5c.6 0 1 .4 1 1 0 1.3.2 2.5.6 3.6.1.3 0 .7-.2 1z"/></svg><span>Telephone: 555-014-2270</span></div>
    <div class="contact-row"><svg width="9" height="9" viewBox="0 0 10 10"><rect x="0" y="3" width="10" height="6" fill="#d8d8d8"/><rect x="2" y="0" width="6" height="3" fill="#d8d8d8"/></svg><span>FAX: 555-014-2271</span></div>
    <div class="contact-row"><svg width="9" height="7" viewBox="0 0 10 8"><rect width="10" height="8" fill="#d8d8d8"/><path d="M0 0l5 4 5-4" stroke="#3b3b3b" fill="none"/></svg><span>info@vardelprec-mfg.example</span></div>
  </div>

  <div class="footer-col" style="left:910px">
    <h4>Follow Us</h4>
    <div class="social" aria-label="Social links"><span></span><span></span><span></span><span></span></div>
    <div class="badges" aria-label="Certification badges">
      <span style="width:58px;height:40px;background:#3f66c4;border-radius:4px"></span>
      <span style="width:42px;height:42px;background:#e5e5e5;border-radius:50%"></span>
    </div>
  </div>

  <div class="footer-rule"></div>
  <p class="copyright">©2019 All Rights Reserved | Privacy Statement. Site Map</p>
</footer>

</body>
</html>
```